Fresh Produce Outlet needs a Poster Design

Hi,
We are Brightleaf Harvest Market, a fruit and veg outlet based in the suburb of Yanchep, Perth, Western Australia.Apart from fresh produce, we also stock nuts and grains, organic products and specialty grocery. We are about to launch a re-branding exercise, projecting ourselves as 'the' shop for fresh produce; quality, taste and freshness being our key differentiators. We are competing against a big supermarket chain who are using marketing muscle power to shut us down and we want to respond with a series of posters which are simple yet bold and sends a clear and positive message to our customers about what we have to offer.
Please feel free to visit our Facebook page www.facebook.com/brightleafharvestmkt to get an idea about our current branding,logo and the shop in general.
Regards
Team - Brightleaf Harvest Market
Target Market(s)
Residents of Yanchep and surrounding suburbs
Industry/Entity Type
Retail
Look and feel

```html
<!DOCTYPE html>
<html lang="en">
<head>
<meta charset="utf-8">
<title>Brightleaf Harvest Market – Always Fresh</title>
<link rel="stylesheet" href="https://fonts.googleapis.com/css2?family=Oswald:wght@400;600&family=Roboto+Condensed:wght@400;700&display=swap">
<style>
  :root {
    --cabbage-light: #c9dc9a;
    --cabbage-mid: #93b45a;
    --cabbage-dark: #4f7a2c;
    --band: rgba(34, 90, 30, 0.78);
    --text: #ffffff;
  }
  html, body {
    margin: 0;
    padding: 0;
    width: 849px;
    height: 1200px;
    overflow: hidden;
  }
  .poster {
    position: relative;
    width: 849px;
    height: 1200px;
    overflow: hidden;
  }
  .produce-photo {
    position: absolute;
    inset: 0;
    background:
      radial-gradient(circle at 25% 20%, var(--cabbage-light) 0%, transparent 35%),
      radial-gradient(circle at 60% 55%, var(--cabbage-light) 0%, transparent 30%),
      radial-gradient(circle at 20% 80%, var(--cabbage-light) 0%, transparent 32%),
      linear-gradient(160deg, var(--cabbage-mid), var(--cabbage-dark));
  }
  .message-band {
    position: absolute;
    top: 0;
    right: 44px;
    width: 316px;
    height: 1200px;
    background: var(--band);
    color: var(--text);
    text-align: center;
    font-family: "Oswald", sans-serif;
  }
  .claims {
    list-style: none;
    margin: 0;
    padding: 92px 0 0;
  }
  .claim {
    margin-bottom: 52px;
    line-height: 1;
  }
  .claim-lead {
    display: block;
    font-family: "Roboto Condensed", sans-serif;
    font-weight: 700;
    font-size: 42px;
    letter-spacing: 1px;
  }
  .claim-word {
    display: block;
    font-family: "Roboto Condensed", sans-serif;
    font-weight: 400;
    font-size: 64px;
    margin-top: 4px;
  }
  .sign-off {
    position: absolute;
    left: 0;
    right: 0;
    top: 860px;
    font-family: "Roboto Condensed", sans-serif;
    font-weight: 700;
  }
  .sign-off-lead {
    font-size: 42px;
    letter-spacing: 1px;
  }
  .brand-mark {
    display: block;
    width: 56px;
    height: 56px;
    margin: 22px auto 18px;
    border-radius: 50%;
    background: #e88a2a;
  }
  .brand-name {
    font-size: 36px;
    line-height: 1.12;
    text-transform: uppercase;
    margin: 0 20px;
  }
</style>
</head>
<body>
  <main class="poster">
    <div class="produce-photo" role="img" aria-label="Close-up photograph of a pile of fresh green cabbages"></div>
    <section class="message-band">
      <ul class="claims">
        <li class="claim"><span class="claim-lead">ALWAYS</span><span class="claim-word">FRESH.</span></li>
        <li class="claim"><span class="claim-lead">ALWAYS</span><span class="claim-word">NATURAL.</span></li>
        <li class="claim"><span class="claim-lead">ALWAYS</span><span class="claim-word">ORGANIC.</span></li>
        <li class="claim"><span class="claim-lead">ALWAYS</span><span class="claim-word">TASTY.</span></li>
      </ul>
      <div class="sign-off">
        <div class="sign-off-lead">ALWAYS</div>
        <span class="brand-mark"></span>
        <div class="brand-name">Brightleaf Harvest Market</div>
      </div>
    </section>
  </main>
</body>
</html>
```